New College Graduate Resume - Creative and unique design that stands out from the rest

Need creative resume design for recent college graduate who graduated from School of Music with a concentration in music composition and production. Striving for a contemporary layout/design that allows the resume to "be unique" and "stand out" but be polished and professional. Open to integrating moderate color/graphics as part of resume design but the design can be minus those attributes as well. Attached is raw content in 7 sections (name/contact info, education, highlights of qualifications, work experience, honors/awards, and professional affiliations). While the designer has full latitude over overall design which (section headers, font type, separation/spacing, use of bullets, justification of text, etc.) please maintain current order/sequence of the 7 sections.

Industry/Entity Type

School

Requirements
Must have
• Name (Tobias Hale Whitcombe II) should be most prominent (bold/font size) compared to remainder of resume copy.
• Section headers should be prominent but less so when compared to name on resume.
• The attached file of resume content is provided as raw source copy and is NOT to be just copied and pasted into open fields as is. Expectation is each section of copy will be organized in a manner that is most visually appealing and may include bullets, appropriate spacing, etc.
Should not have
• The attached file of resume content is provided as source copy and is NOT to be just copied and pasted into open fields as is. Expectation is each section of copy will be organized in a manner that

```html
<!DOCTYPE html>
<html lang="en">
<head>
<meta charset="utf-8">
<title>Tobias Hale Whitcombe II – Resume</title>
<link href="https://fonts.googleapis.com/css2?family=Oswald:wght@500;600;700&family=Open+Sans:wght@400;600;700&display=swap" rel="stylesheet">
<style>
:root{
  --backdrop:#efe9e1;
  --paper:#ffffff;
  --ink:#2c2a3a;
  --purple:#4a4470;
  --purple-deep:#3b3461;
  --lavender:#e8e6f1;
  --rule:#9d98bd;
}
*{box-sizing:border-box;margin:0;padding:0}
html,body{width:1200px;height:783px;overflow:hidden;background:var(--backdrop)}
.resume{
  position:absolute;left:310px;top:16px;width:580px;height:751px;
  background:var(--paper);display:flex;overflow:hidden;
  box-shadow:0 6px 18px rgba(60,50,40,.18);
  font-family:"Open Sans",sans-serif;color:var(--ink);
}
.sidebar{width:212px;flex:none;background:var(--purple);color:var(--lavender);padding:20px 16px 16px 18px}
.main{flex:1;padding:22px 22px 18px 22px}
.section-title{
  font-family:"Oswald",sans-serif;font-weight:600;text-transform:uppercase;
  letter-spacing:.3px;line-height:1.05;
}
.sidebar .section-title{color:#fff;font-size:17px;margin:0 0 6px}
.main .section-title{color:var(--purple-deep);font-size:16px;margin:16px 0 8px}
.profile-text{font-size:7.6px;line-height:1.45;text-align:justify;margin-bottom:14px}
.dot-list{list-style:none;font-size:7.6px;line-height:1.45;margin-bottom:14px}
.dot-list li{position:relative;padding-left:12px}
.dot-list li::before{content:"";position:absolute;left:1px;top:4.5px;width:4px;height:4px;border-radius:50%;background:var(--lavender)}
.dot-list .sub::before{display:none}
.timeline{list-style:none;position:relative;margin-left:4px;padding-left:14px;border-left:1px solid var(--rule)}
.timeline li{position:relative;margin-bottom:6px;font-size:7.6px;line-height:1.4}
.timeline li:last-child{margin-bottom:0}
.timeline li::before{content:"";position:absolute;left:-17.5px;top:3px;width:6px;height:6px;border-radius:50%;background:var(--lavender)}
.sidebar .timeline{margin-bottom:14px}
.sidebar .timeline:last-child{margin-bottom:0}
.name{font-family:"Oswald",sans-serif;font-weight:700;font-size:25px;line-height:1;color:var(--purple-deep);text-transform:uppercase;letter-spacing:.2px;white-space:nowrap}
.contact{list-style:none;margin-top:8px;font-size:8px;line-height:1.6}
.contact li{display:flex;align-items:center;gap:6px}
.contact svg{width:9px;height:9px;flex:none}
.main .timeline{border-color:var(--purple-deep)}
.main .timeline li{font-size:8.2px;line-height:1.45;margin-bottom:9px}
.main .timeline li:last-child{margin-bottom:0}
.main .timeline li::before{background:var(--purple-deep)}
.job{margin-bottom:10px;font-size:8.2px;line-height:1.5}
.job-org{font-weight:700;color:var(--purple-deep)}
.job-role{font-weight:700}
.job p{margin-top:1px}
</style>
</head>
<body>
<article class="resume">
  <aside class="sidebar">
    <h2 class="section-title">Profile</h2>
    <p class="profile-text">Recent graduate of a highly ranked university seeking opportunities to apply composition and production talents across a variety of music genres and media. Expertise lies in delivering high quality sound design, editing, mixing and recording. Excellent interpersonal skills and the ability to build strong relationships with people of all levels. Exceptionally motivated self-starter and creative problem solver who enjoys working collaboratively on teams.</p>

    <h2 class="section-title">Highlights of<br>Qualifications</h2>
    <ul class="dot-list">
      <li>Media Production Software</li>
      <li class="sub">(StudioTrack 11)</li>
      <li>Sound Design</li>
      <li>Sound Acoustics</li>
      <li>Studio Recording</li>
      <li>Audio Editing</li>
      <li>Audio Mixing</li>
      <li>Analog/Digital board operation</li>
      <li>Music Arrangement</li>
      <li>Music Composition</li>
      <li>Music Production</li>
      <li>Composing Sheet Music</li>
      <li>Singer-songwriter</li>
      <li>Rhythm guitarist</li>
    </ul>

    <h2 class="section-title">Honors/Awards</h2>
    <ul class="timeline">
      <li>Best Film and Score: Reels and Scores 2015 Competition (Bayside University)</li>
      <li>Ellis R. Langford Scholar</li>
      <li>Best New Member, Delta Kappa Omicron Fraternity, Inc.</li>
      <li>Bayside University Homecoming King, 2012</li>
    </ul>

    <h2 class="section-title">Professional<br>Affiliations</h2>
    <ul class="timeline">
      <li>Member, Guild of Screen Composers (GSC)</li>
      <li>Member, Songwriters and Publishers Alliance (SPA)</li>
      <li>Member, Audio Craft Society (ACS)</li>
      <li>Member, Delta Kappa Omicron Fraternity, Incorporated</li>
    </ul>
  </aside>

  <main class="main">
    <h1 class="name">Tobias Hale Whitcombe II</h1>
    <ul class="contact">
      <li><svg viewBox="0 0 10 10"><circle cx="5" cy="5" r="5" fill="#3b3461"/><path d="M5 2.2a1.9 1.9 0 0 0-1.9 1.9C3.1 5.6 5 7.8 5 7.8s1.9-2.2 1.9-3.7A1.9 1.9 0 0 0 5 2.2z" fill="#fff"/></svg>82 Larkspur Lane, Atlanta, Georgia 30300</li>
      <li><svg viewBox="0 0 10 10"><circle cx="5" cy="5" r="5" fill="#3b3461"/><rect x="3.4" y="2.2" width="3.2" height="5.6" rx=".6" fill="#fff"/></svg>555-014-7146</li>
      <li><svg viewBox="0 0 10 10"><circle cx="5" cy="5" r="5" fill="#3b3461"/><rect x="2.4" y="3.2" width="5.2" height="3.6" fill="#fff"/><path d="M2.4 3.2 5 5.2l2.6-2" stroke="#3b3461" stroke-width=".6" fill="none"/></svg>thwhitcombe@mailbox.example</li>
    </ul>

    <h2 class="section-title">Education</h2>
    <ul class="timeline">
      <li>Bayside University – Harmon School of Music<br>Seabrook, Florida</li>
      <li>Bachelor of Music – May 2016<br>Major: Media Writing and Production, GPA 3.20/4.0</li>
      <li>Eastbrook Academy<br>College Park, Georgia<br>High School Diploma with Honors – May 2011</li>
    </ul>

    <h2 class="section-title">Work Experience</h2>
    <div class="job">
      <div class="job-org">Coral Reel Studios (CRS)</div>
      <div>Miami, FL<br>May 2014 – Present</div>
      <div class="job-role">Sound Engineer</div>
      <p>Edited and mixed recorded field audio to professional standards. Matched audio with motion picture video to create a seamless product. Recorded automated dialogue replacement (ADR) audio and integrated into motion picture video project using StudioTrack 11. Recorded foley sound effects to be added to film, video, and other media in post-production. Composed and recorded original music to accompany various video projects.</p>
    </div>
    <div class="job">
      <div class="job-org">Brightline Retail</div>
      <div>Atlanta, GA<br>May 2013 – October 2013</div>
      <div class="job-role">Sales Associate</div>
      <p>Provided customer service, maintained a clean and organized work environment, assisted in sales, and performed cashier responsibilities.</p>
    </div>
    <div class="job">
      <div class="job-org">Peachtree Civic Research Group</div>
      <div>Atlanta, GA<br>June 2012 – August 2012</div>
      <div class="job-role">On-Site Promoter/Intern</div>
      <p>Promoted and advertised various campaigns and managed various office tasks, such as setting up site maps and organizing and sorting non-profit donations.</p>
    </div>
    <div class="job">
      <div class="job-org">Keystone Direct Sales, Incorporated</div>
      <div>Atlanta, GA<br>June 2011 – August 2011</div>
      <div class="job-role">Product Marketing Consultant</div>
      <p>Conducted direct sales and marketing of subsidiary product line through establishing a compelling value proposition, overcoming objections, and closing the sale.</p>
    </div>
  </main>
</article>
</body>
</html>
```